Patient Transport company website design

We're a small patient transport company desiring a big company image. Our company is called Pelnorva. We're based in Houston, TX. Our mission is to provide a safe, cost effective, and convenient mode of local transportation. Similar to a taxi service but more patient friendly.
We would like to see designs that illustrate our mission and have a big company online presence. We like bright colors but not too bright and cartoon-like. Our target audience are patients but we also cater to elderly as well as those who might not have reliable transportation.
We're not an emergency transport service. We're not a taxi service. We're more like a shuttle service... a compromise between the two. Photography for the site should show patients and elderly riding in normal (unmarked vehicles) to and from dr visits, etc.
Our competitors' websites are listed here to give you a general idea about the industry.
http://www.trelvanridecare.example/
http://www.brivashuttle.example/
http://www.quomelwayshuttles.example/
Target Market(s)
Patients needing transportation assistance and Elderly as well.
Industry/Entity Type
Taxi
Requirements
Must have
- Website must be done in wordpress. Website must have the following links:
Services, About, Book a trip, jobs, control panel, clients
Should use photos communicating safe travels to and from... particularly with Elderly if possible.
Design should be consistent with attached logo.
Nice to have
- Bright colors

```html
<!DOCTYPE html>
<html lang="en">
<head>
<meta charset="utf-8">
<title>Pelnorva — Patient Transportation Services</title>
<link rel="stylesheet" href="https://fonts.googleapis.com/css2?family=Source+Sans+3:wght@300;400;600&display=swap">
<style>
  :root {
    --page-bg: #efefef;
    --white: #ffffff;
    --navy: #123f87;
    --navy-dark: #0d3374;
    --blue: #1a8bc4;
    --cyan: #1aa0d0;
    --green: #8cc63f;
    --green-dark: #6fae22;
    --title-blue: #1a4e92;
    --text: #6d6d6d;
    --text-dark: #4a4a4a;
    --border: #d9d9d9;
  }
  * { box-sizing: border-box; margin: 0; padding: 0; }
  html, body { width: 1071px; height: 1200px; overflow: hidden; }
  body {
    position: relative;
    background: var(--page-bg);
    font-family: "Source Sans 3", sans-serif;
    font-weight: 300;
    color: var(--text);
  }
  .page { position: absolute; left: 89px; top: 0; width: 908px; height: 1100px; background: var(--white); }

  .brand { position: absolute; left: 25px; top: 30px; display: flex; align-items: center; gap: 16px; }
  .brand-mark { width: 96px; height: 62px; border-radius: 50%; background: var(--green); }
  .brand-name { font-size: 42px; font-weight: 400; color: var(--title-blue); line-height: 1; }
  .brand-tagline { font-size: 10px; font-weight: 400; color: var(--cyan); letter-spacing: 1px; margin-top: 4px; }

  .callout { position: absolute; right: 24px; top: 48px; text-align: right; }
  .callout-label { font-size: 20px; color: var(--green); font-weight: 400; line-height: 1; }
  .callout-phone { font-size: 24px; color: var(--cyan); font-weight: 400; line-height: 1.1; margin-top: 4px; }

  .main-nav { position: absolute; left: 0; top: 112px; width: 908px; height: 43px;
    background: linear-gradient(#1d55a6, var(--navy-dark)); display: flex; }
  .main-nav a { color: var(--white); text-decoration: none; font-size: 17px; font-weight: 400;
    line-height: 43px; padding: 0 20px; border-right: 1px solid #0a2a60; }
  .main-nav a:first-child { padding-left: 28px; }
  .main-nav a:last-child { border-right: 0; }

  .hero { position: absolute; left: 0; top: 155px; width: 908px; height: 341px; }
  .hero-photo { position: absolute; inset: 0;
    background: linear-gradient(180deg, #a9c3d6 0%, #7f946f 35%, #8d8c86 65%, #c9c6bd 100%); }
  .hero-banner { position: absolute; left: 0; top: 182px; width: 560px; height: 101px; }
  .hero-text { position: absolute; left: 23px; top: 200px; color: var(--white); }
  .hero-title { font-size: 31px; font-weight: 400; line-height: 1.1; }
  .hero-sub { font-size: 20px; font-weight: 300; margin-top: 8px; }
  .hero-dot { position: absolute; left: 422px; top: 318px; width: 14px; height: 14px; border-radius: 50%; background: #c6e21a; }

  .feature { position: absolute; top: 521px; width: 280px; height: 256px; border: 1px solid var(--border);
    border-radius: 3px; background: var(--white); padding: 14px 16px; }
  .feature-photo { height: 119px; border: 1px solid #bbb; }
  .feature-title { font-size: 22px; font-weight: 400; margin-top: 8px; line-height: 1.2; }
  .feature-text { font-size: 11.5px; line-height: 20px; margin-top: 4px; }
  .btn { display: inline-block; margin-top: 7px; width: 88px; height: 28px; line-height: 28px; text-align: center;
    color: var(--white); font-size: 13px; font-weight: 400; border-radius: 3px; }
  .btn-cyan { background: linear-gradient(#2fb0e0, #1489bd); }
  .btn-green { background: linear-gradient(#9ed24c, #70ae23); }
  .btn-navy { background: linear-gradient(#2461b5, #0f3c86); }
  .t-cyan { color: var(--cyan); } .t-green { color: var(--green-dark); } .t-navy { color: var(--title-blue); }

  .welcome { position: absolute; left: 29px; top: 828px; width: 568px; }
  .welcome h1 { font-size: 27px; font-weight: 400; color: var(--title-blue); }
  .welcome h2 { font-size: 17px; font-weight: 300; color: var(--text-dark); margin-top: 6px; }
  .welcome p { font-size: 12.5px; line-height: 21.3px; margin-top: 7px; }
  .welcome p + p { margin-top: 9px; }

  .services-box { position: absolute; left: 612px; top: 807px; width: 281px; height: 237px;
    border: 1px solid var(--border); border-radius: 3px; background: linear-gradient(#fff 60%, #f0f0f0); padding: 20px 35px 0 30px; }
  .services-box h3 { font-size: 24px; font-weight: 400; color: var(--green-dark); line-height: 1; }
  .services-list { list-style: none; margin-top: 14px; }
  .services-list li { display: flex; align-items: center; gap: 9px; font-size: 12.5px; height: 26.6px; border-bottom: 1px solid #e2e2e2; }
  .services-list li:last-child { border-bottom: 0; }
  .services-list svg { flex: none; }

  .site-footer { position: absolute; left: 0; top: 1100px; width: 1071px; height: 100px; background: var(--navy); }
  .footer-nav { position: absolute; left: 112px; top: 22px; font-size: 14.5px; font-weight: 400; color: var(--white); }
  .footer-nav span { margin: 0 6px; }
  .copyright { position: absolute; left: 113px; top: 51px; font-size: 11.5px; color: #9fb0cf; }
  .social { position: absolute; left: 855px; top: 24px; display: flex; gap: 7px; }
  .social span { width: 21px; height: 21px; border-radius: 2px; background: #4a78c2; }
  .social span:nth-child(2) { background: #3fb3e6; }
  .social span:nth-child(3) { background: #2a73b3; }
  .social span:nth-child(4) { background: #f08b1d; }
</style>
</head>
<body>
<div class="page">
  <header>
    <div class="brand">
      <div class="brand-mark"></div>
      <div>
        <div class="brand-name">Pelnorva</div>
        <div class="brand-tagline">Patient Transportation Services</div>
      </div>
    </div>
    <div class="callout">
      <div class="callout-label">Call Us Now</div>
      <div class="callout-phone">555.014.2290</div>
    </div>
  </header>

  <nav class="main-nav">
    <a>Home</a><a>About Us</a><a>Patient Transportation</a><a>Services</a><a>Testimonials</a><a>Hire Us</a><a>Support</a><a>Contact</a>
  </nav>

  <section class="hero">
    <div class="hero-photo" role="img" aria-label="Street scene with an ambulance, patrol car and responders outside apartment buildings"></div>
    <svg class="hero-banner" viewBox="0 0 560 101" aria-hidden="true">
      <polygon points="420,0 485,0 530,50 485,101 420,101" fill="#1a9fd0"/>
      <polygon points="0,0 465,0 510,50 465,101 0,101" fill="#8cc63f"/>
    </svg>
    <div class="hero-text">
      <div class="hero-title">Patient Transportation Services</div>
      <div class="hero-sub">We Provide 24/7 Patient Transportation</div>
    </div>
    <div class="hero-dot"></div>
  </section>

  <article class="feature" style="left:18px">
    <div class="feature-photo" role="img" aria-label="Medics moving a patient on a stretcher outside a house" style="background:linear-gradient(135deg,#4f8a5a,#b8c6a8 55%,#6b6b6b)"></div>
    <div class="feature-title t-cyan">Cost Effective</div>
    <p class="feature-text">Morbi eget arcu. Morbi porta, libero id ullamcorper nonummy, nibh ligula pulvinar metus</p>
    <span class="btn btn-cyan">Learn More</span>
  </article>
  <article class="feature" style="left:315px">
    <div class="feature-photo" role="img" aria-label="Crew loading a patient into an ambulance" style="background:linear-gradient(135deg,#3d4a3a,#d8d6d0 50%,#8a8f80)"></div>
    <div class="feature-title t-green">Patient Transportation</div>
    <p class="feature-text">Morbi eget arcu. Morbi porta, libero id ullamcorper nonummy, nibh ligula pulvinar metus</p>
    <span class="btn btn-green">Learn More</span>
  </article>
  <article class="feature" style="left:612px">
    <div class="feature-photo" role="img" aria-label="Paramedics attending to a patient on a stretcher" style="background:linear-gradient(135deg,#556b8a,#c88a4a 50%,#9aa3b3)"></div>
    <div class="feature-title t-navy">Provide Safely</div>
    <p class="feature-text">Morbi eget arcu. Morbi porta, libero id ullamcorper nonummy, nibh ligula pulvinar metus</p>
    <span class="btn btn-navy">Learn More</span>
  </article>

  <section class="welcome">
    <h1>Welcome to Our Website Mainpage..</h1>
    <h2>Proin nulla arcu nonummy luctus dictum eget fermentum et lorem</h2>
    <p>Duis tincidunt lectus quis dui viverra vestibulum. Suspendisse vulputate aliquam dui. Nulla elementum dui ut augue. Aliquam vehicula mi at mauris. Maecenas placerat, nisl at consequat rhoncus, sem nunc gravida justo, quis eleifend arcu velit quis lacus. Morbi magna magna, tincidunt a, mattis non, imperdiet vitae, tellus. Sed odio est, auctor ac, sollicitudin in, consequat vitae, orci.</p>
    <p>Donec scelerisque leo ac risus. Praesent sit amet est. In dictum, dolor eu dictum porttitor, enim felis viverra mi, eget luctus massa purus quis odio. Etiam nulla massa, pharetra facilisis, volutpat in</p>
  </section>

  <aside class="services-box">
    <h3>Services We Provide</h3>
    <ul class="services-list">
      <li><svg width="16" height="16" viewBox="0 0 16 16"><circle cx="8" cy="8" r="8" fill="#7cbf2e"/><path d="M4.2 8.3l2.6 2.5 5-5.2" stroke="#fff" stroke-width="2" fill="none"/></svg>Vivamus porttitor nisi eleifend</li>
      <li><svg width="16" height="16" viewBox="0 0 16 16"><circle cx="8" cy="8" r="8" fill="#7cbf2e"/><path d="M4.2 8.3l2.6 2.5 5-5.2" stroke="#fff" stroke-width="2" fill="none"/></svg>Libero tempus libero lectus feugiat</li>
      <li><svg width="16" height="16" viewBox="0 0 16 16"><circle cx="8" cy="8" r="8" fill="#7cbf2e"/><path d="M4.2 8.3l2.6 2.5 5-5.2" stroke="#fff" stroke-width="2" fill="none"/></svg>Morbi diam mauris viverra</li>
      <li><svg width="16" height="16" viewBox="0 0 16 16"><circle cx="8" cy="8" r="8" fill="#7cbf2e"/><path d="M4.2 8.3l2.6 2.5 5-5.2" stroke="#fff" stroke-width="2" fill="none"/></svg>Morbi eget arcu</li>
      <li><svg width="16" height="16" viewBox="0 0 16 16"><circle cx="8" cy="8" r="8" fill="#7cbf2e"/><path d="M4.2 8.3l2.6 2.5 5-5.2" stroke="#fff" stroke-width="2" fill="none"/></svg>Morbi porta libero id ullamcorper</li>
      <li><svg width="16" height="16" viewBox="0 0 16 16"><circle cx="8" cy="8" r="8" fill="#7cbf2e"/><path d="M4.2 8.3l2.6 2.5 5-5.2" stroke="#fff" stroke-width="2" fill="none"/></svg>Ligula pulvinar metus eget</li>
    </ul>
  </aside>
</div>

<footer class="site-footer">
  <div class="footer-nav">Home<span>|</span>About Us<span>|</span>Patient Transportation<span>|</span>Services<span>|</span>Testimonials<span>|</span>Hire Us<span>|</span>Support<span>|</span>Contact</div>
  <div class="copyright">Copyright © 2013 Company Name.&nbsp; All right reserved</div>
  <div class="social"><span></span><span></span><span></span><span></span></div>
</footer>
</body>
</html>
```